SEO AND WEB DESIGN COMPANY BUSINESS CARD DESIGN

I need an eye catching , simple business card design that will match my logo . I need 2 versions of it ( white background and black background) - SOME PEOPLE DID NOT GET IT AND SENDING US FRONT WHITE BACK WHITE VERSIONS WHICH IS NOT CORRECT.

ONE VERSION SHOULD BE BACK AND FRONT ALL BLACK , SECOND VERSION SHOULD BE BACK AND FRONT ALL WHITE

logo psd files are attached for both versions. The business card is going to have : First Name- Last name - position - phone numbers

```html
<!DOCTYPE html>
<html lang="en">
<head>
<meta charset="utf-8">
<title>Business Card – Black Version</title>
<link rel="stylesheet" href="https://fonts.googleapis.com/css2?family=Oswald:wght@300;400;500;600&display=swap">
<style>
  :root {
    --page-bg: #ececed;
    --card-bg: #0b0b0b;
    --ink: #ffffff;
    --accent: #4f8fd6;
  }
  * { margin: 0; padding: 0; box-sizing: border-box; }
  html, body {
    width: 1200px;
    height: 800px;
    overflow: hidden;
    background: var(--page-bg);
  }
  .canvas {
    position: relative;
    width: 1200px;
    height: 800px;
  }
  .card {
    position: absolute;
    top: 278px;
    width: 419px;
    height: 240px;
    background: var(--card-bg);
    color: var(--ink);
    font-family: "Oswald", "Arial Narrow", sans-serif;
  }
  .card--front { left: 142px; }
  .card--back  { left: 637px; }

  .contact {
    position: absolute;
    left: 0;
    right: 0;
    text-align: center;
    white-space: nowrap;
  }
  .contact__name {
    top: 56px;
    font-size: 43px;
    font-weight: 600;
    line-height: 52px;
    letter-spacing: -0.6px;
  }
  .contact__position {
    top: 104px;
    font-size: 27px;
    font-weight: 300;
    line-height: 32px;
  }
  .contact__phone {
    top: 150px;
    font-size: 28px;
    font-weight: 400;
    line-height: 36px;
    letter-spacing: 0.2px;
  }

  .brand {
    position: absolute;
    inset: 0;
    display: flex;
    align-items: center;
    justify-content: center;
    gap: 14px;
  }
  .brand__dot {
    flex: none;
    width: 30px;
    height: 30px;
    border-radius: 50%;
    background: var(--accent);
  }
  .brand__name {
    font-size: 62px;
    font-weight: 500;
    line-height: 1;
    color: var(--ink);
    letter-spacing: 0.5px;
    white-space: nowrap;
  }
</style>
</head>
<body>
  <main class="canvas">
    <section class="card card--front">
      <p class="contact contact__name">YOUR NAME</p>
      <p class="contact contact__position">POSITION</p>
      <p class="contact contact__phone">123 456 7890</p>
    </section>
    <section class="card card--back">
      <div class="brand">
        <span class="brand__dot"></span>
        <span class="brand__name">MARLOWIND</span>
      </div>
    </section>
  </main>
</body>
</html>
```